Case Study Template

We would like a template for case studies that we can then use whenever we do a great job for our clients to help future clients understand what we do.

Whilst we could just use the word version provided we feel there is probably opportunity to have a much more professionally designed look feel for the template.

The finished case studies will be printed on glossy and used as sales collateral as well as being posted on the web as part of our web based information.

The template needs to be in MS word or MS powerpoint so that we can easily produce new case studies into the future using the template format.

The attached incorporates the basic structure with the initial section providing some context, then 3 main sections (boxes) for the the actual case study detail.

Very open to different convention if you have experience in this regard.....

Target Market(s)

Small to medium business owners and their advisors (Accountants, Bankers, Consultants)

Industry/Entity Type

Sales

Requirements
Must have
• We need the caption at the bottom referring to Tovrin being a holder of Australian Credit License ..... as this is a regulatory requirement.

It must have our logo in the design

```html
<!DOCTYPE html>
<html lang="en">
<head>
<meta charset="utf-8">
<title>Tovrin Case Study</title>
<link rel="stylesheet" href="https://fonts.googleapis.com/css2?family=Carlito:wght@400;700&display=swap">
<style>
  :root {
    --backdrop: #595959;
    --paper: #ffffff;
    --navy: #2b3f58;
    --teal: #2a7a9b;
    --cell: #dcdcdc;
    --ink: #3a3a3a;
    --title-ink: #3d4a58;
    --white: #ffffff;
    --link: #1a3cc4;
  }
  * { box-sizing: border-box; margin: 0; padding: 0; }
  html, body { width: 1200px; height: 1000px; overflow: hidden; }
  body {
    background: var(--backdrop);
    font-family: "Carlito", Calibri, Arial, sans-serif;
    position: relative;
  }
  .page {
    position: absolute; left: 372px; top: 178px;
    width: 457px; height: 644px; background: var(--paper);
  }
  .brand {
    position: absolute; left: 30px; top: 30px;
    font-size: 20px; font-weight: 700; color: var(--navy);
  }
  .doc-type {
    position: absolute; right: 27px; top: 53px;
    font-size: 7px; color: var(--ink); letter-spacing: .3px;
  }
  .banner {
    position: absolute; left: 28px; top: 72px; width: 404px; height: 110px;
    background: linear-gradient(90deg, #e6edf3 0%, #d3dde7 45%, #8fa4b8 75%, #5d7890 100%);
  }
  .banner-band {
    position: absolute; left: 0; top: 22px; width: 262px; height: 68px;
    background: rgba(255,255,255,.45);
  }
  .banner-title {
    position: absolute; left: 4px; top: 28px; width: 258px;
    font-size: 13px; line-height: 19.5px; font-weight: 700; color: var(--title-ink);
  }
  .facts { position: absolute; left: 27px; top: 188px; width: 128px; }
  .fact-label {
    background: var(--navy); color: var(--white);
    font-size: 10px; font-weight: 700; height: 13px; line-height: 13px; padding-left: 5px;
  }
  .fact-value {
    background: var(--cell); color: var(--ink);
    font-size: 9px; line-height: 11px; padding: 5px 5px 4px; margin-bottom: 1px;
  }
  .fact-value.summary { padding-bottom: 7px; }
  .details {
    position: absolute; left: 166px; top: 188px; width: 264px; height: 386px;
    background: var(--navy); color: var(--white);
  }
  .section-head {
    background: var(--teal); font-size: 10px; font-weight: 700;
    height: 13px; line-height: 13px; padding-left: 5px;
  }
  .section-list {
    list-style: disc; padding: 5px 14px 6px 35px;
    font-size: 8.6px; line-height: 11.4px; font-weight: 700;
  }
  .footer-rule {
    position: absolute; left: 23px; top: 599px; width: 412px; height: 1px; background: var(--ink);
  }
  .legal {
    position: absolute; left: 28px; top: 607px; font-size: 5.2px; line-height: 7px; color: var(--navy);
  }
  .legal a { color: var(--link); }
</style>
</head>
<body>
  <article class="page">
    <div class="brand">Tovrin</div>
    <div class="doc-type">CASE STUDY</div>

    <header class="banner" role="img" aria-label="Financial photograph of coins resting on market charts">
      <div class="banner-band"></div>
      <h1 class="banner-title">Helping businesses to solve bank problems Lowering costs and improving access to funding</h1>
    </header>

    <aside class="facts">
      <div class="fact-label">Tovrin Service</div>
      <div class="fact-value">Finance Restructure</div>
      <div class="fact-label">Industry</div>
      <div class="fact-value">Furniture Wholesaler</div>
      <div class="fact-label">Turnover</div>
      <div class="fact-value">$3M</div>
      <div class="fact-label">Executive Summary</div>
      <div class="fact-value summary">Tovrin procures a material increase in cheaper funding for a client unable to find funding themselves</div>
    </aside>

    <section class="details">
      <h2 class="section-head">Situation Appraisal</h2>
      <ul class="section-list">
        <li>Growing business with increasing import requirements.</li>
        <li>Client applied for an increase in funding directly with the house bank and were told further security was required. One Owner/Director already had his home in the security mix and no further security was readily available.</li>
        <li>Corvane Advisory Partner introduced Tovrin, who were later engaged to undertake a financial and banking diagnostic/review.</li>
      </ul>
      <h2 class="section-head">Outcomes/Benefits Delivered</h2>
      <ul class="section-list">
        <li>Post diagnostic, Tovrin completed a financing proposal paper and targeted specific financiers.</li>
        <li>Increased offer of facilities received from an alternative financier. 30% increase in Working Capital facilities.</li>
        <li>Release of personal home from the business security negotiated.</li>
        <li>Review of Facility Documentation and refinance effected.</li>
        <li>Additional temporary funding subsequently provided by the new bank.</li>
        <li>Client achieved a financing result well in excess of what they expected due to their relationship with their Accountant (Corvane Advisory!).</li>
      </ul>
      <h2 class="section-head">Future Opportunities</h2>
      <ul class="section-list">
        <li>No requirement for ongoing Bank Management support required given current CFO ability and reasonably straight forward business reporting.</li>
        <li>Potential for virtual CFO offering upon retirement of CFO/Finance Director.</li>
        <li>Ad hoc catch up with client and Bank to ensure relationship running smoothly and provide assistance when the CFO transition occurs.</li>
      </ul>
    </section>

    <div class="footer-rule"></div>
    <footer class="legal">
      <p>Tovrin Financial Services Pty Ltd holds Australian Credit License No. 381204.</p>
      <p>To find out more about Tovrin Financial Services Pty Ltd visit our website at <a href="#">www.tovrinfinance.com.au</a> or call us on +61 3 9555 0182</p>
    </footer>
  </article>
</body>
</html>
```